Business Card Design

building company specialistloft conversion,extension ,bathrooms ,kitchens ,painting and decorating all general building work

Industry/Entity Type

Building

Contact Information for Business Card

K&R Home renewal Ltd
tel -07912468305
email-Rmarek07@brickmail.example
web in progres

Font styles to use
Sans Serif

Requirements
Must have
• name of the company
• all contact details
Nice to have
• some of the skills

```html
<!DOCTYPE html>
<html lang="en">
<head>
<meta charset="utf-8">
<title>K&amp;R Home renewal Ltd — Business Card</title>
<link rel="stylesheet" href="https://fonts.googleapis.com/css2?family=Montserrat:wght@400;500;600;700&display=swap">
<style>
  :root {
    --page: #ecebea;
    --card-black: #1b1b1c;
    --pattern-tone: #262627;
    --panel-dark: #2c2c2d;
    --panel-mid: #474748;
    --gold: #b08a3e;
    --white: #f2f2f2;
    --soft: #d4d4d4;
  }
  * { box-sizing: border-box; margin: 0; padding: 0; }
  html, body { width: 1200px; height: 800px; overflow: hidden; }
  body {
    background: var(--page);
    font-family: "Montserrat", Arial, sans-serif;
    position: relative;
  }
  .card {
    position: absolute;
    top: 240px;
    width: 540px;
    height: 309px;
    background: var(--card-black);
    box-shadow: 0 6px 18px rgba(0,0,0,0.25);
    overflow: hidden;
  }
  .card--back { left: 40px; }
  .card--front { left: 620px; }

  .brand-block {
    position: absolute;
    display: flex;
    align-items: center;
    gap: 12px;
  }
  .brand-mark { width: 14px; height: 14px; background: var(--gold); flex: none; }
  .brand-name {
    color: var(--gold);
    font-weight: 600;
    font-size: 18px;
    letter-spacing: 0.5px;
    white-space: nowrap;
  }

  /* back */
  .back-pattern {
    position: absolute;
    left: 130px;
    top: 20px;
    width: 280px;
    height: 250px;
    background: radial-gradient(ellipse at center, var(--pattern-tone) 0%, var(--pattern-tone) 45%, var(--card-black) 72%);
  }
  .card--back .brand-block--centre {
    left: 50%;
    top: 118px;
    transform: translateX(-50%);
    gap: 14px;
  }
  .brand-block--centre .brand-mark { width: 22px; height: 22px; }
  .brand-block--centre .brand-name { font-size: 24px; }
  .card--back .brand-block--corner { left: 34px; bottom: 30px; }

  /* front */
  .front-panels { position: absolute; inset: 0; }
  .card--front .brand-block { left: 34px; top: 114px; }
  .card--front .brand-mark { width: 34px; height: 34px; }
  .card--front .brand-name { font-size: 20px; }
  .holder {
    position: absolute;
    right: 26px;
    top: 176px;
    text-align: right;
  }
  .holder-name {
    font-weight: 700;
    font-size: 24px;
    letter-spacing: 1px;
    text-transform: uppercase;
    color: var(--white);
    margin-bottom: 12px;
  }
  .holder-name .surname { color: var(--gold); }
  .contact-line {
    display: flex;
    justify-content: flex-end;
    align-items: center;
    gap: 10px;
    color: var(--soft);
    font-size: 15px;
    line-height: 25px;
  }
  .contact-line svg { width: 16px; height: 16px; fill: var(--soft); flex: none; }
</style>
</head>
<body>

<section class="card card--back" aria-label="Card back">
  <div class="back-pattern" role="img" aria-label="Faint dark geometric background pattern"></div>
  <div class="brand-block brand-block--centre">
    <span class="brand-mark"></span>
    <span class="brand-name">K&amp;R Home renewal Ltd</span>
  </div>
  <div class="brand-block brand-block--corner">
    <span class="brand-name">K&amp;R Home renewal Ltd</span>
  </div>
</section>

<section class="card card--front" aria-label="Card front">
  <svg class="front-panels" viewBox="0 0 540 309" preserveAspectRatio="none" aria-hidden="true">
    <polygon points="290,0 540,0 540,70" fill="var(--panel-dark)"/>
    <polygon points="540,30 540,309 300,309" fill="var(--panel-mid)"/>
  </svg>

  <div class="brand-block">
    <span class="brand-mark"></span>
    <span class="brand-name">K&amp;R Home renewal Ltd</span>
  </div>

  <div class="holder">
    <p class="holder-name">Rafal <span class="surname">Marek</span></p>
    <p class="contact-line">07912468305
      <svg viewBox="0 0 24 24"><path d="M6.6 10.8a15.1 15.1 0 0 0 6.6 6.6l2.2-2.2c.3-.3.7-.4 1-.2 1.1.4 2.3.6 3.6.6.6 0 1 .4 1 1V20c0 .6-.4 1-1 1A17 17 0 0 1 3 4c0-.6.4-1 1-1h3.5c.6 0 1 .4 1 1 0 1.3.2 2.5.6 3.6.1.3 0 .7-.2 1z"/></svg>
    </p>
    <p class="contact-line">Rmarek07@brickmail.example
      <svg viewBox="0 0 24 24"><path d="M2 5h20v14H2zm2 2v.5l8 5 8-5V7zm0 3v7h16v-7l-8 5z"/></svg>
    </p>
  </div>
</section>

</body>
</html>
```